Professional Oral Surgery Referral Pad, Business Card, and Stationary Design

Hello,

I want to work with a designer for my startup Oral Surgery Practice called: Dorrel Creek Oral Surgery & Implant Center

Ideally I would like to choose a good/professional design and work with a designer all the way to fulfill ALL of our stationary needs including referral pads, business cards, letterheads, envelopes, notepads, email signature, etc.

I would like to see designs first and hopefully would like to work with the designer for the lifetime of my practice and wanting to develop a long-term professional relationship.

In terms of the logo I have attached our practice logo files: I want to stay within the 3 colorways of the logo: Navy Blue/Silver grey/White. I would like for you to be creative and incorporate the "V" as best you can (for example greyed out watermark, etc)

I have also attached in my files the full contact info of our office in a word document: which includes address, email address, phone, fax, cell, etc.

I have also attached a few examples of double sided referral pad we can draw inspiration from. In terms of the referral pad I would ideally like to have my logo nicely placed/incorporated to make it look professional, address of the practice and contact info, my name and credentials.

Referral pad must have lines for patient, date of birth, phone number, referring doctor name, odontogram of all adult teeth and pediatric teeth, nice and big - so easy for dentist to refer. Also a jaw drawing of the intraoral cavity. Below that should have comments to surgeon.

In terms of procedures, I would like to have options of IV sedation, extractions, wisdom teeth, bone graft, pathology, tmj, trauma, expose/bond, orthognathic, other (list below)

In the back we can have a greyed out map of my practice address and Instructions for patients should include to bring insurance documentation, medication list, etc.

The final nitty gritty details of the referral pad can be worked on once I am happy with the design.

Target Market(s)

Patients who need oral surgical services and dentist referrals

Industry/Entity Type

Oral and Maxillofacial Surgery

• I would leave it up to the designers!

Colors
0054AA
0677BA
7BADD7
CADEEF
E8F1F8

Requirements
Must have
• Professional/sleek/modern and three color ways same as logo (navy blue, silver gray, and white)
Nice to have
• I would like to highlight my logo especially the implant ā€œvā€ either as watermark or part of the header or footnote. I will leave it to the expertise of the designer

```html
<!DOCTYPE html>
<html lang="en">
<head>
<meta charset="utf-8">
<title>Dorrel Creek Oral Surgery – Referral Pad</title>
<link rel="stylesheet" href="https://fonts.googleapis.com/css2?family=Cormorant+Garamond:wght@600&family=Encode+Sans:ital,wght@0,300;0,400;0,700;1,300&display=swap">
<style>
:root{
  --navy:#0b3f91;
  --blue:#0d4ea3;
  --ink:#555a60;
  --rule:#6c7076;
  --sheet-edge:#d4d6da;
  --map:#e4e7ec;
  --chart:#f1f2f4;
  --white:#ffffff;
}
*{box-sizing:border-box;margin:0;padding:0}
html,body{width:1200px;height:1200px;overflow:hidden;background:var(--white)}
body{font-family:"Encode Sans",sans-serif}
.stage{position:absolute;left:0;top:0;width:1930px;height:1930px;transform:scale(0.62176);transform-origin:0 0}
.sheet{position:absolute;width:797px;height:1231px;background:var(--white);border:1px solid var(--sheet-edge);box-shadow:0 22px 24px -18px rgba(0,0,0,.28)}
.sheet--front{left:148px;top:181px}
.sheet--back{left:987px;top:520px}
.abs{position:absolute}

/* header */
.header{left:0;top:67px;width:797px;height:178px;background:var(--navy);color:var(--white)}
.brand{left:44px;top:42px;width:310px;text-align:center;font-family:"Cormorant Garamond",serif;font-weight:600;color:var(--white)}
.brand__name{font-size:31px;line-height:36px;letter-spacing:1px}
.brand__sub{font-size:31px;line-height:36px;letter-spacing:1px}
.header__divider{left:372px;top:30px;width:2px;height:122px;background:rgba(255,255,255,.7)}
.contact{left:408px;top:36px;font-style:italic;font-weight:300;font-size:17px;line-height:22.5px}
.contact__doctor{font-size:18px;margin-bottom:1px;padding-left:6px}
.contact__row{display:flex;align-items:center;gap:8px}
.contact__row svg{width:16px;height:16px;fill:var(--white)}

/* form */
.field{left:37px;width:378px;display:flex;align-items:flex-end;font-size:20px;color:var(--blue);line-height:24px}
.field__line{flex:1;border-bottom:1.3px solid var(--rule);margin-left:18px;margin-bottom:3px}
.rule{height:0;border-bottom:1.3px solid var(--rule)}
.check{display:flex;align-items:center;font-size:20px;line-height:24px}
.box{display:inline-block;width:17px;height:17px;border:1.5px solid var(--ink);margin-right:4px;flex:none}
.check--blue{color:var(--blue)}
.check--grey{color:var(--ink);font-weight:300}
.vline{width:2px;background:var(--navy)}
.chart{left:452px;top:254px;width:287px;height:432px;background:var(--chart);border-radius:6px}

.section-title{font-size:20px;font-weight:700;color:var(--navy);letter-spacing:.3px}
.footer-rule{left:62px;top:1146px;width:675px;height:2px;background:linear-gradient(90deg,rgba(11,63,145,0),var(--navy) 25%,var(--navy) 75%,rgba(11,63,145,0))}
.footer-note{left:0;top:1156px;width:797px;text-align:center;font-size:15.5px;line-height:20.5px;color:#7a7e84;font-weight:300}

/* back */
.back-heading{width:797px;left:0;text-align:center;font-size:22.5px;color:var(--navy);letter-spacing:.3px}
.back-text{left:58px;width:690px;font-size:17px;line-height:26.6px;color:var(--ink);font-weight:300}
.back-text b{font-weight:700;color:#4a4e54}
.back-center{left:0;width:797px;text-align:center;font-size:17px;line-height:31px;color:var(--ink);font-weight:300}
.back-center .call{font-weight:700;color:#4a4e54}
.back-center .blue{color:var(--navy);font-weight:400}
.map{left:144px;top:870px;width:509px;height:288px;background:linear-gradient(135deg,#e9ecf0,var(--map));box-shadow:0 2px 6px rgba(0,0,0,.2)}
.back-address{left:0;width:797px;top:1172px;display:flex;justify-content:center;align-items:center;gap:8px;font-size:17px;color:var(--navy)}
.back-address svg{width:13px;height:16px;fill:var(--navy)}
</style>
</head>
<body>
<div class="stage">

  <!-- FRONT -->
  <section class="sheet sheet--front">
    <header class="abs header">
      <div class="abs brand">
        <div class="brand__name">Dorrel Creek</div>
        <div class="brand__sub">Oral Surgery</div>
        <div class="brand__name" style="font-size:19px;letter-spacing:4px">&amp; IMPLANT CENTER</div>
      </div>
      <div class="abs header__divider"></div>
      <div class="abs contact">
        <div class="contact__doctor">Dr. Anika Rowe, DDS</div>
        <div class="contact__row"><svg viewBox="0 0 16 16"><path d="M8 1a5 5 0 0 0-5 5c0 4 5 9 5 9s5-5 5-9a5 5 0 0 0-5-5zm0 7a2 2 0 1 1 0-4 2 2 0 0 1 0 4z"/></svg>118 Larkspur Ave, Dorrel Creek, CA 90210</div>
        <div class="contact__row"><svg viewBox="0 0 16 16"><path d="M3.6 1.5l2.3 2.6-1.2 1.8c.9 2 2.4 3.5 4.4 4.4l1.8-1.2 2.6 2.3-1.6 2.1C6.7 13.1 2.9 9.3 1.5 3.1z"/></svg>555 014 2270</div>
        <div class="contact__row"><svg viewBox="0 0 16 16"><path d="M4 1h8v4H4zM1 6h14v6h-3v3H4v-3H1zm4 5v3h6v-3z"/></svg>555 014 2281</div>
        <div class="contact__row"><svg viewBox="0 0 16 16"><path d="M1 3h14v10H1zm1.5 1.2L8 8.6l5.5-4.4z"/></svg>info@dorrelcreekos.com</div>
      </div>
    </header>

    <div class="abs field" style="top:309px">Introducing<span class="field__line"></span></div>
    <div class="abs field" style="top:346px">Date<span class="field__line"></span></div>
    <div class="abs field" style="top:383px">Patient Phone<span class="field__line"></span></div>
    <div class="abs field" style="top:419px">DOB<span class="field__line"></span></div>
    <div class="abs check check--blue" style="left:36px;top:456px"><span class="box"></span>Call to appoint<span class="box" style="margin-left:22px"></span>Patient will call</div>
    <div class="abs check check--blue" style="left:36px;top:493px"><span class="box"></span>Appointment made by referring doctor</div>
    <div class="abs field" style="top:530px">Referring Doctor<span class="field__line"></span></div>
    <div class="abs rule" style="left:37px;top:585px;width:378px"></div>
    <div class="abs field" style="top:604px">Phone<span class="field__line"></span></div>

    <div class="abs vline" style="left:442px;top:277px;height:387px"></div>
    <div class="abs chart" role="img" aria-label="Odontogram: open-mouth intraoral drawing above adult teeth 1–32 and pediatric teeth A–T"></div>

    <div class="abs section-title" style="left:37px;top:700px">FACIAL PROCEDURES</div>
    <div class="abs" style="left:36px;top:732px">
      <div class="check check--grey" style="height:30.5px"><span class="box"></span>Orthognathic Evaluation</div>
      <div class="check check--grey" style="height:30.5px"><span class="box"></span>Sleep Apnea</div>
      <div class="check check--grey" style="height:30.5px"><span class="box"></span>TMJ Evaluation</div>
      <div class="check check--grey" style="height:30.5px"><span class="box"></span>Pathology</div>
      <div class="check check--grey" style="height:30.5px"><span class="box"></span>Cleft Lip, Palate Evaluation</div>
      <div class="check check--grey" style="height:30.5px"><span class="box"></span>Facial Trauma</div>
      <div class="check check--grey" style="height:30.5px"><span class="box"></span>Other<span class="rule" style="width:178px;margin-left:12px;margin-top:14px"></span></div>
    </div>

    <div class="abs section-title" style="left:34px;top:957px">Radiographs</div>
    <div class="abs" style="left:36px;top:996px">
      <div class="check check--grey" style="height:30.5px"><span class="box"></span>Emailed: info@dorrelcreekos.com</div>
      <div class="check check--grey" style="height:30.5px"><span class="box"></span>Given to Patient</div>
      <div class="check check--grey" style="height:30.5px"><span class="box"></span>Mailed</div>
      <div class="check check--grey" style="height:30.5px"><span class="box"></span>Please Take</div>
    </div>

    <div class="abs vline" style="left:359px;top:719px;height:390px"></div>

    <div class="abs section-title" style="left:369px;top:700px">ORAL SURGERY PROCEDURES</div>
    <div class="abs" style="left:368px;top:732px">
      <div class="check check--grey" style="height:30.5px"><span class="box"></span>Extraction, Tooth #</div>
      <div class="check check--grey" style="height:30.5px"><span class="box"></span>Wisdom Teeth Removal #</div>
      <div class="check check--grey" style="height:30.5px"><span class="box"></span>Evaluation For Implants</div>
      <div class="check check--grey" style="height:30.5px"><span class="box"></span>Exposure of Tooth #</div>
      <div class="check check--grey" style="height:30.5px"><span class="box"></span>Other<span class="rule" style="width:305px;margin-left:12px;margin-top:14px"></span></div>
    </div>
    <div class="abs rule" style="left:369px;top:903px;width:391px"></div>
    <div class="abs rule" style="left:369px;top:935px;width:391px"></div>

    <div class="abs section-title" style="left:368px;top:957px;display:flex;width:392px;align-items:flex-end">Notes<span class="rule" style="flex:1;margin-left:8px;margin-bottom:3px"></span></div>
    <div class="abs rule" style="left:369px;top:1010px;width:391px"></div>
    <div class="abs rule" style="left:369px;top:1045px;width:391px"></div>
    <div class="abs rule" style="left:369px;top:1079px;width:391px"></div>
    <div class="abs rule" style="left:369px;top:1114px;width:391px"></div>

    <div class="abs footer-rule"></div>
    <p class="abs footer-note">Please see the reverse for additional information and a map to our office.<br>Please bring any x-rays and insurance information with you to your appointment.</p>
  </section>

  <!-- BACK -->
  <section class="sheet sheet--back">
    <h2 class="abs back-heading" style="top:112px;font-weight:400">INSTRUCTIONS FOR YOUR FIRST VISIT</h2>
    <div class="abs back-text" style="top:145px">
      <p>• Please bring all x-rays, this referral slip, pertinent medical information and a list of ALL medications you are currently taking.</p>
      <p>• Please alert the office if you have a medical condition that may be of concern prior to surgery. (Bleeding disorders, heart conditions, taking blood thinners, etc.)</p>
      <p>• Please bring a photo ID and both your medical and dental insurance cards on the day of your appointment.</p>
      <p>• Patients under eighteen (18) years of age must be accompanied by a parent or legal guardian at the time of the initial consult and surgery.</p>
    </div>
    <h2 class="abs back-heading" style="top:367px;font-weight:400">INSTRUCTIONS FOR GENERAL ANESTHESIA</h2>
    <div class="abs back-text" style="top:400px;line-height:27px">
      <p><b>PLEASE NOTE:</b> In most instances, sedation and surgery are not performed at the first appointment. Typically, the patient is seen first for consultation and surgery is scheduled for a separate appointment. <b>The following only applies if surgery with sedation is done at the first appointment:</b></p>
    </div>
    <div class="abs back-text" style="left:53px;top:517px;width:700px">
      <p>• Do not eat or drink anything 8 hours prior to your surgery, NO FOOD OR DRINK, including water, unless directed by your doctor.</p>
      <p>• Most daily medications may be taken prior to surgery with only a SIP of WATER. Please call our office if you have any questions regarding your medications.</p>
      <p>• Any patient under 18 years of age must be accompanied by a parent or legal guardian. Wear loose, comfortable clothing with sleeves that can be raised above your elbow. Avoid slippers and sandals.</p>
      <p>• If you require corrective lenses, please wear your glasses. No contacts.</p>
    </div>
    <div class="abs back-center" style="top:735px">
      <p class="call">Please call our office with any questions! 555 014 2270</p>
      <p class="blue" style="margin-top:3px">YOU MUST BE ACCOMPANIED BY SOMEONE TO DRIVE YOU</p>
      <p class="blue">HOME &amp; STAY WITH YOU FOR SIX HOURS AFTER SURGERY</p>
      <p>Please give 48 hours notice if you are unable to keep this appointment.</p>
    </div>
    <div class="abs map" role="img" aria-label="Grey street map marking the practice at 118 Larkspur Ave"></div>
    <div class="abs back-address"><svg viewBox="0 0 13 16"><path d="M6.5 0A6 6 0 0 0 .5 6c0 4.5 6 10 6 10s6-5.5 6-10a6 6 0 0 0-6-6zm0 8.5a2.5 2.5 0 1 1 0-5 2.5 2.5 0 0 1 0 5z"/></svg>118 Larkspur Ave, Dorrel Creek, CA 90210</div>
  </section>

</div>
</body>
</html>
```